Personal Development Model Graphic

I am creating a Personal Development/Coaching business and website and need some assistance with the development of a graphic that represents my methodology. I have already done what I consider to be a working version, but now it's time to have a professional design eye take a look at it and improve.

Specifically, I need assistance on color usage. I'd like each of the 8 areas of the model to have a color, and I've tried to utilize colors I feel are representative of the specific area(for example, purple for spirituality) but it doesn't really work for everything and perhaps additional thought could be put to that aspect of it.

Also, the model needs to work in reverse of the way it's pictured in the attached JPEG. So Friends needs to be first (top center)and then going clockwise, Spirituality needs to be in the 1:00 position not the 11:00 position and then continue around to Community, Family, Exercise, Career, Art/Creativity, and last at 11:00 Sexuality. I was going to update it before uploading, but I'm having trouble with Photoshop and just decided to pull the trigger on having a designer do it.

Thank you in advance for your creativity and ideas!

Industry/Entity Type

Business

Requirements
Nice to have
• It would be fantastic if it could feel modern, and high tech. I realize this is difficult with circles! But whatever you can do.

On color usage, it would again be wonderful to have colors that are more modern than traditional. I'll leave that to your discretion.

```html
<!DOCTYPE html>
<html lang="en">
<head>
<meta charset="utf-8">
<title>Happiness Model</title>
<link rel="stylesheet" href="https://fonts.googleapis.com/css2?family=Oswald:wght@500&display=swap">
<style>
  :root {
    --bg: #02131f;
    --ring: #d9d9d9;
    --ring-shade: #9a9a9a;
    --label: #f4f0ec;
    --core-text: #eafaff;

    --friends-hi: #e88a2a;  --friends: #a85200;  --friends-lo: #5e2c00;
    --spirit-hi: #b25ad8;   --spirit: #7a1f9a;   --spirit-lo: #4a0c62;
    --community-hi: #18d070;--community: #08863e; --community-lo: #034a22;
    --family-hi: #ff9a40;   --family: #ff5f0a;   --family-lo: #c43a00;
    --exercise-hi: #ffc84a; --exercise: #f08c00; --exercise-lo: #b85a00;
    --career-hi: #3a78ff;   --career: #0e3ad0;   --career-lo: #061e7a;
    --art-hi: #e84848;      --art: #b80808;      --art-lo: #6a0000;
    --sex-hi: #ff4cc0;      --sex: #cc0a82;      --sex-lo: #7a004a;
    --core-hi: #5fe0ff;     --core: #0ea0d6;     --core-lo: #05628e;
  }
  html, body {
    margin: 0;
    padding: 0;
    overflow: hidden;
    background: var(--bg);
  }
  .canvas {
    width: 1200px;
    height: 1000px;
    background: var(--bg);
    position: relative;
    overflow: hidden;
  }
  .model { display: block; }
  .ring { fill: none; stroke: var(--ring); stroke-width: 15; }
  .ring-edge { fill: none; stroke: var(--ring-shade); stroke-width: 2; opacity: .6; }
  .area-label {
    font-family: "Oswald", "Arial Narrow", sans-serif;
    font-weight: 500;
    font-size: 33px;
    fill: var(--label);
    text-anchor: middle;
    dominant-baseline: central;
    letter-spacing: -0.5px;
  }
  .core-label {
    font-family: "Oswald", "Arial Narrow", sans-serif;
    font-weight: 500;
    font-size: 88px;
    fill: var(--core-text);
    text-anchor: middle;
    dominant-baseline: central;
  }
  .gloss { fill: url(#gloss); }
  .sheen { fill: none; stroke: #ffffff; stroke-opacity: .12; }
</style>
</head>
<body>
<div class="canvas">
<svg class="model" width="1200" height="1000" viewBox="0 0 1200 1000" xmlns="http://www.w3.org/2000/svg" role="img" aria-label="Happiness at the centre, fed by Friends, Spirituality, Community, Family, Exercise, Career, Art/Creativity and Sexuality">
  <defs>
    <radialGradient id="gloss" cx="40%" cy="20%" r="60%">
      <stop offset="0" stop-color="#fff" stop-opacity=".45"/>
      <stop offset="1" stop-color="#fff" stop-opacity="0"/>
    </radialGradient>
    <radialGradient id="g-friends" cx="35%" cy="28%" r="75%"><stop offset="0" style="stop-color:var(--friends-hi)"/><stop offset=".6" style="stop-color:var(--friends)"/><stop offset="1" style="stop-color:var(--friends-lo)"/></radialGradient>
    <radialGradient id="g-spirit" cx="35%" cy="28%" r="75%"><stop offset="0" style="stop-color:var(--spirit-hi)"/><stop offset=".6" style="stop-color:var(--spirit)"/><stop offset="1" style="stop-color:var(--spirit-lo)"/></radialGradient>
    <radialGradient id="g-community" cx="35%" cy="28%" r="75%"><stop offset="0" style="stop-color:var(--community-hi)"/><stop offset=".6" style="stop-color:var(--community)"/><stop offset="1" style="stop-color:var(--community-lo)"/></radialGradient>
    <radialGradient id="g-family" cx="35%" cy="28%" r="75%"><stop offset="0" style="stop-color:var(--family-hi)"/><stop offset=".6" style="stop-color:var(--family)"/><stop offset="1" style="stop-color:var(--family-lo)"/></radialGradient>
    <radialGradient id="g-exercise" cx="35%" cy="28%" r="75%"><stop offset="0" style="stop-color:var(--exercise-hi)"/><stop offset=".6" style="stop-color:var(--exercise)"/><stop offset="1" style="stop-color:var(--exercise-lo)"/></radialGradient>
    <radialGradient id="g-career" cx="35%" cy="28%" r="75%"><stop offset="0" style="stop-color:var(--career-hi)"/><stop offset=".6" style="stop-color:var(--career)"/><stop offset="1" style="stop-color:var(--career-lo)"/></radialGradient>
    <radialGradient id="g-art" cx="35%" cy="28%" r="75%"><stop offset="0" style="stop-color:var(--art-hi)"/><stop offset=".6" style="stop-color:var(--art)"/><stop offset="1" style="stop-color:var(--art-lo)"/></radialGradient>
    <radialGradient id="g-sex" cx="35%" cy="28%" r="75%"><stop offset="0" style="stop-color:var(--sex-hi)"/><stop offset=".6" style="stop-color:var(--sex)"/><stop offset="1" style="stop-color:var(--sex-lo)"/></radialGradient>
    <radialGradient id="g-core" cx="35%" cy="25%" r="80%"><stop offset="0" style="stop-color:var(--core-hi)"/><stop offset=".55" style="stop-color:var(--core)"/><stop offset="1" style="stop-color:var(--core-lo)"/></radialGradient>
    <!-- arrow pointing toward the centre, drawn in the 12 o'clock slot -->
    <path id="arrow" d="M590 256 H610 V278 H622 L600 302 L578 278 H590 Z"/>
  </defs>

  <!-- connecting ring -->
  <circle class="ring" cx="600" cy="500" r="358"/>
  <circle class="ring-edge" cx="600" cy="500" r="366"/>

  <!-- arrows -->
  <g class="arrows">
    <use href="#arrow" style="fill:var(--friends)"/>
    <use href="#arrow" style="fill:var(--spirit)" transform="rotate(45 600 500)"/>
    <use href="#arrow" style="fill:var(--community)" transform="rotate(90 600 500)"/>
    <use href="#arrow" style="fill:var(--family)" transform="rotate(135 600 500)"/>
    <use href="#arrow" style="fill:var(--exercise)" transform="rotate(180 600 500)"/>
    <use href="#arrow" style="fill:var(--career)" transform="rotate(225 600 500)"/>
    <use href="#arrow" style="fill:var(--art)" transform="rotate(270 600 500)"/>
    <use href="#arrow" style="fill:var(--sex)" transform="rotate(315 600 500)"/>
  </g>

  <!-- life areas -->
  <g class="area area-friends">
    <circle cx="600" cy="140" r="108" fill="url(#g-friends)"/>
    <ellipse class="gloss" cx="600" cy="92" rx="86" ry="56"/>
    <circle class="sheen" cx="600" cy="140" r="96" stroke-width="10"/>
    <text class="area-label" x="600" y="142">FRIENDS</text>
  </g>
  <g class="area area-spirituality">
    <circle cx="852" cy="246" r="108" fill="url(#g-spirit)"/>
    <ellipse class="gloss" cx="852" cy="198" rx="86" ry="56"/>
    <circle class="sheen" cx="852" cy="246" r="96" stroke-width="10"/>
    <text class="area-label" x="852" y="246">SPIRITUALITY</text>
  </g>
  <g class="area area-community">
    <circle cx="958" cy="498" r="108" fill="url(#g-community)"/>
    <ellipse class="gloss" cx="958" cy="450" rx="86" ry="56"/>
    <circle class="sheen" cx="958" cy="498" r="96" stroke-width="10"/>
    <text class="area-label" x="958" y="498">COMMUNITY</text>
  </g>
  <g class="area area-family">
    <circle cx="852" cy="750" r="108" fill="url(#g-family)"/>
    <ellipse class="gloss" cx="852" cy="702" rx="86" ry="56"/>
    <circle class="sheen" cx="852" cy="750" r="96" stroke-width="10"/>
    <text class="area-label" x="852" y="750">FAMILY</text>
  </g>
  <g class="area area-exercise">
    <circle cx="600" cy="858" r="108" fill="url(#g-exercise)"/>
    <ellipse class="gloss" cx="600" cy="810" rx="86" ry="56"/>
    <circle class="sheen" cx="600" cy="858" r="96" stroke-width="10"/>
    <text class="area-label" x="600" y="855">EXERCISE</text>
  </g>
  <g class="area area-career">
    <circle cx="348" cy="750" r="108" fill="url(#g-career)"/>
    <ellipse class="gloss" cx="348" cy="702" rx="86" ry="56"/>
    <circle class="sheen" cx="348" cy="750" r="96" stroke-width="10"/>
    <text class="area-label" x="348" y="750">CAREER</text>
  </g>
  <g class="area area-art">
    <circle cx="243" cy="498" r="108" fill="url(#g-art)"/>
    <ellipse class="gloss" cx="243" cy="450" rx="86" ry="56"/>
    <circle class="sheen" cx="243" cy="498" r="96" stroke-width="10"/>
    <text class="area-label" x="243" y="480">ART/</text>
    <text class="area-label" x="243" y="518">CREATIVITY</text>
  </g>
  <g class="area area-sexuality">
    <circle cx="348" cy="246" r="108" fill="url(#g-sex)"/>
    <ellipse class="gloss" cx="348" cy="198" rx="86" ry="56"/>
    <circle class="sheen" cx="348" cy="246" r="96" stroke-width="10"/>
    <text class="area-label" x="348" y="246">SEXUALITY</text>
  </g>

  <!-- centre -->
  <g class="core">
    <circle cx="600" cy="500" r="190" fill="url(#g-core)"/>
    <ellipse class="gloss" cx="600" cy="415" rx="150" ry="100"/>
    <circle class="sheen" cx="600" cy="500" r="172" stroke-width="18"/>
    <text class="core-label" x="600" y="497" textLength="316" lengthAdjust="spacingAndGlyphs">HAPPINESS</text>
  </g>
</svg>
</div>
</body>
</html>
```